Motor Vault Website - Part of the Brantley Group

A complimentary website is required for the launch of a 'Motor Vault' - a new service launched by industry renowned BRANTLEY. Motor Vault is an industry-first brand that designs and builds unique subterranean car parks for private residential homes in London and the influential counties within the UK. Please see here the direction of a new BRANTLEY Website - we would like Motor Vault to be complimentary and sit alongside BRANTLEY harmoniously - https://www.brantleyhomes.example/brantley-nu-staging Brantley have some images, but whilst more professional images are in production - we have also attached pixmora photos- named clearly as pixmora. **Attached files include JPEG, .eps of logo and Brantley library images and Pixmora Library Images - two versions of logo dependent on background colour. - Website needs to be sleek, chic and masculine.- Colour Palette - Grey/ Black/ White - Same visiual journey as Brantley website- Required areas within the sit include - About Us / Our Work / Contact Page

Target Market(s)

Luxury
Men

Number of Pages Required

2 page

Font styles to use
Sans Serif

Colors
e8e8e8
757575
1b1b1b
000000
9d9d9d
cbcbcb
f5f5f5

Requirements
Must have
• Complimentary of this site - https://www.brantleyhomes.example/brantley-nu-staging
Should not have
• Colour

```html
<!DOCTYPE html>
<html lang="en">
<head>
<meta charset="utf-8">
<title>Motor Vault – Part of the Brantley Group</title>
<link rel="stylesheet" href="https://fonts.googleapis.com/css2?family=Libre+Baskerville:wght@400;700&family=Work+Sans:wght@300;400;500&display=swap">
<style>
  :root {
    --black: #000000;
    --ink: #1b1b1b;
    --grey-dark: #757575;
    --grey-mid: #9d9d9d;
    --grey-light: #cbcbcb;
    --grey-pale: #e8e8e8;
    --section-bg: #f0f0f0;
    --white: #ffffff;
    --serif: 'Libre Baskerville', Georgia, serif;
    --sans: 'Work Sans', Arial, sans-serif;
  }
  * { margin: 0; padding: 0; box-sizing: border-box; }
  html, body { width: 1200px; height: 2719px; overflow: hidden; }
  body { position: relative; background: var(--white); font-family: var(--sans); color: var(--ink); }

  .brand { display: inline-flex; flex-direction: column; align-items: flex-end; }
  .brand-name { display: flex; align-items: center; gap: 10px; font-family: var(--sans); font-weight: 500; letter-spacing: 1px; line-height: 1; }
  .brand-mark { display: inline-block; }
  .brand-sub { font-family: var(--sans); font-weight: 400; letter-spacing: 0.5px; margin-top: 4px; }

  /* Hero */
  .hero { position: absolute; left: 0; top: 0; width: 1200px; height: 553px; overflow: hidden; }
  .hero-photo { position: absolute; inset: 0; background: radial-gradient(ellipse at 50% 45%, #6f6f6f 0%, #3c3c3c 40%, #161616 100%); }
  .hero-content { position: absolute; left: 0; right: 0; top: 205px; text-align: center; color: var(--white); }
  .hero .brand-name { font-size: 56px; color: var(--white); }
  .hero .brand-mark { width: 34px; height: 34px; background: var(--white); }
  .hero .brand-sub { font-size: 10px; color: var(--grey-light); }
  .hero-tagline { margin-top: 28px; font-family: var(--serif); font-size: 17px; letter-spacing: 1.5px; color: var(--white); }
  .hero-arrow { position: absolute; left: 589px; top: 498px; }

  /* Navigation */
  .site-nav { position: absolute; left: 0; top: 553px; width: 1200px; height: 97px; background: var(--white); box-shadow: 0 2px 6px rgba(0,0,0,0.06); }
  .site-nav .brand { position: absolute; left: 87px; top: 28px; }
  .site-nav .brand-name { font-size: 38px; color: var(--ink); }
  .site-nav .brand-mark { width: 26px; height: 26px; background: var(--ink); }
  .site-nav .brand-sub { font-size: 7px; color: var(--grey-dark); }
  .nav-links { position: absolute; right: 84px; top: 40px; display: flex; gap: 20px; list-style: none; font-size: 11px; letter-spacing: 2.5px; color: var(--ink); }
  .nav-links li.sep { color: var(--grey-dark); letter-spacing: 0; }
  .nav-links .current { font-weight: 500; border-bottom: 1px solid var(--ink); padding-bottom: 2px; }

  /* Welcome */
  .welcome { position: absolute; left: 0; top: 650px; width: 1200px; height: 605px; background: var(--white); }
  .welcome-photo { position: absolute; left: 236px; top: 81px; width: 296px; height: 445px; background: linear-gradient(135deg, #2a2a2a 0%, #8d8d8d 45%, #3a3a3a 75%, #111 100%); }
  .corner { position: absolute; width: 38px; height: 38px; border-color: var(--white); border-style: solid; }
  .corner.tl { left: 18px; top: 18px; border-width: 1px 0 0 1px; }
  .corner.br { right: 18px; bottom: 18px; border-width: 0 1px 1px 0; }
  .welcome-text { position: absolute; left: 610px; top: 134px; width: 400px; text-align: center; }
  .welcome-text h1 { font-family: var(--serif); font-weight: 400; font-size: 43px; line-height: 1.18; letter-spacing: 2px; color: var(--black); }
  .rule { display: block; width: 62px; height: 2px; background: var(--grey-mid); margin: 0 auto; }
  .welcome-text .rule { margin-top: 24px; margin-bottom: 26px; }
  .welcome-text p { font-size: 15px; line-height: 1.8; color: var(--ink); padding: 0 36px; }
  .btn { display: inline-block; background: var(--black); color: var(--white); font-family: var(--sans); font-size: 12px; letter-spacing: 2px; text-transform: uppercase; text-align: center; line-height: 46px; height: 46px; }
  .welcome-text .btn { margin-top: 30px; width: 238px; }

  /* Our work */
  .our-work { position: absolute; left: 0; top: 1255px; width: 1200px; height: 600px; background: var(--section-bg); text-align: center; }
  .section-title { font-family: var(--serif); font-weight: 400; font-size: 28px; letter-spacing: 2px; color: var(--black); padding-top: 74px; }
  .our-work .rule { margin-top: 18px; }
  .work-grid { position: absolute; left: 87px; top: 166px; display: flex; gap: 26px; list-style: none; }
  .work-item { width: 325px; }
  .work-photo { width: 325px; height: 232px; }
  .work-photo.one { background: linear-gradient(160deg, #9a9a9a 0%, #3a3a3a 40%, #121212 100%); }
  .work-photo.two { background: linear-gradient(200deg, #b5b5b5 0%, #5a5a5a 45%, #1a1a1a 100%); }
  .work-photo.three { background: linear-gradient(140deg, #2c2c2c 0%, #6d6d6d 55%, #1c1c1c 100%); }
  .work-item h3 { font-family: var(--serif); font-weight: 400; font-size: 17px; letter-spacing: 1.5px; margin-top: 25px; color: var(--black); }
  .our-work .btn { position: absolute; left: 481px; top: 473px; width: 238px; }

  /* Slider */
  .feature-slider { position: absolute; left: 0; top: 1855px; width: 1200px; height: 509px; overflow: hidden; }
  .slider-photo { position: absolute; inset: 0; background: linear-gradient(180deg, #2b2b2b 0%, #6b6b6b 35%, #8a8a8a 60%, #3a3a3a 100%); }
  .slide-caption { position: absolute; left: 277px; top: 133px; width: 648px; height: 245px; background: rgba(27,27,27,0.72); text-align: center; color: var(--white); }
  .slide-caption h2 { font-family: var(--serif); font-weight: 400; font-size: 28px; letter-spacing: 2px; margin-top: 34px; }
  .slide-caption .rule { background: var(--grey-light); margin-top: 18px; margin-bottom: 22px; }
  .slide-caption p { font-size: 14.5px; line-height: 1.85; padding: 0 36px; color: var(--grey-pale); }
  .slider-arrow { position: absolute; top: 239px; }
  .slider-arrow.prev { left: 16px; }
  .slider-arrow.next { right: 16px; }

  /* Footer */
  .site-footer { position: absolute; left: 0; top: 2364px; width: 1200px; height: 355px; background: var(--ink); text-align: center; color: var(--grey-mid); }
  .site-footer .brand { margin-top: 73px; }
  .site-footer .brand-name { font-size: 42px; color: var(--white); }
  .site-footer .brand-mark { width: 28px; height: 28px; background: var(--white); }
  .site-footer .brand-sub { font-size: 7px; color: var(--grey-light); }
  .social-links { display: flex; justify-content: center; gap: 20px; list-style: none; margin-top: 42px; }
  .social-links li { width: 44px; height: 44px; display: flex; align-items: center; justify-content: center; }
  .social-links span { width: 32px; height: 32px; background: var(--grey-dark); transform: rotate(45deg); display: block; }
  .footer-address { margin-top: 40px; font-size: 10.5px; letter-spacing: 1.5px; }
  .footer-legal { margin-top: 16px; font-size: 10.5px; letter-spacing: 1.5px; }
</style>
</head>
<body>

<header class="hero">
  <div class="hero-photo" role="img" aria-label="Black and white photograph of an empty concrete underground car park with columns receding into the distance"></div>
  <div class="hero-content">
    <div class="brand">
      <span class="brand-name"><span class="brand-mark"></span>MOTOR VAULT</span>
      <span class="brand-sub">PART OF THE BRANTLEY GROUP</span>
    </div>
    <p class="hero-tagline">BUILDS UNIQUE SUBTERRANEAN CAR PARKS</p>
  </div>
  <svg class="hero-arrow" width="22" height="32" viewBox="0 0 22 32" aria-hidden="true">
    <path d="M11 2 V29 M3 21 L11 29 L19 21" fill="none" stroke="#ffffff" stroke-width="2"/>
  </svg>
</header>

<nav class="site-nav">
  <div class="brand">
    <span class="brand-name"><span class="brand-mark"></span>MOTOR VAULT</span>
    <span class="brand-sub">PART OF THE BRANTLEY GROUP</span>
  </div>
  <ul class="nav-links">
    <li class="current">HOME</li><li class="sep">/</li>
    <li>ABOUT US</li><li class="sep">/</li>
    <li>OUR WORK</li><li class="sep">/</li>
    <li>CONTACT</li>
  </ul>
</nav>

<section class="welcome">
  <div class="welcome-photo" role="img" aria-label="Black and white close-up photograph of a car alloy wheel and brake disc">
    <span class="corner tl"></span>
    <span class="corner br"></span>
  </div>
  <div class="welcome-text">
    <h1>WELCOME TO MOTOR VAULT</h1>
    <span class="rule"></span>
    <p>All the Lorem Ipsum generators on the Internet tend to repeat predefined chunks as necessary, making this the first true generator on the Internet.</p>
    <span class="btn">Read more about us</span>
  </div>
</section>

<section class="our-work">
  <h2 class="section-title">OUR WORK</h2>
  <span class="rule"></span>
  <ul class="work-grid">
    <li class="work-item">
      <div class="work-photo one" role="img" aria-label="Black and white photograph of workers inside a construction site with light beams"></div>
      <h3>LOREM IPSUM DUMMY</h3>
    </li>
    <li class="work-item">
      <div class="work-photo two" role="img" aria-label="Black and white photograph looking up at a steel girder structure"></div>
      <h3>CONTRARY POPULAR BELIEF</h3>
    </li>
    <li class="work-item">
      <div class="work-photo three" role="img" aria-label="Black and white photograph of a welder working among steel beams with sparks"></div>
      <h3>STANDARD CHUNK LOREM</h3>
    </li>
  </ul>
  <span class="btn">View more our work</span>
</section>

<section class="feature-slider">
  <div class="slider-photo" role="img" aria-label="Black and white photograph of an underground excavation with machinery and timber supports"></div>
  <div class="slide-caption">
    <h2>LOREM IPSUM DUMMY PRINTING</h2>
    <span class="rule"></span>
    <p>Lorem Ipsum is simply dummy text of the printing and typesetting industry. Lorem Ipsum has been the industry's standard dummy text ever since the 1500s, when an unknown printer took a galley of type and scrambled it to make a type specimen book.</p>
  </div>
  <svg class="slider-arrow prev" width="24" height="40" viewBox="0 0 24 40" aria-hidden="true">
    <path d="M20 3 L4 20 L20 37" fill="none" stroke="#ffffff" stroke-width="2"/>
  </svg>
  <svg class="slider-arrow next" width="24" height="40" viewBox="0 0 24 40" aria-hidden="true">
    <path d="M4 3 L20 20 L4 37" fill="none" stroke="#ffffff" stroke-width="2"/>
  </svg>
</section>

<footer class="site-footer">
  <div class="brand">
    <span class="brand-name"><span class="brand-mark"></span>MOTOR VAULT</span>
    <span class="brand-sub">PART OF THE BRANTLEY GROUP</span>
  </div>
  <ul class="social-links" aria-label="Social links">
    <li><span></span></li>
    <li><span></span></li>
    <li><span></span></li>
    <li><span></span></li>
  </ul>
  <p class="footer-address">42 HARLOW YARD, LONDON, W9 8QT | TEL: 0207 555 0182</p>
  <p class="footer-legal">COPYRIGHT © MOTORVAULT 2019. TERMS AND CONDITIONS | PRIVACY POLICY</p>
</footer>

</body>
</html>
```